Bright Harbour Mortgages Social Media Campaign

I need social media campaign banners. Facebook and Instagram.
I would like them to incorporate local photos, my photo and my logo. I have some sample files of previous campaigns and I have a color scheme associated with my brand. My business operates in St. John's Newfoundland.

Target Market(s)

Home Buyers, Home Owners

Industry/Entity Type

Mortgage Brokering

Logo Text

Bright Harbour Mortgages

Logo styles of interest
Lettermark Logo
Font styles to use
Other font styles liked:
• Times New Roman, I'm open to suggestion

Colors
0054AA
0677BA
7BADD7
CADEEF
E8F1F8
EE7325
F08F49
F5BC92
FAE3D3
FDF4ED

Requirements
Must have
• My name, photo, contact info, slogan
Nice to have
• We can discuss slogans to use, I can provide some suggestions.

```html
<!DOCTYPE html>
<html lang="en">
<head>
<meta charset="utf-8">
<title>Bright Harbour Mortgages – Social Banners</title>
<link rel="stylesheet" href="https://fonts.googleapis.com/css2?family=Poppins:wght@400;600;700;800&display=swap">
<style>
  :root{
    --sheet:#dcdcdc;
    --white:#ffffff;
    --navy:#071650;
    --orange:#f2460f;
    --ink:#1f1f24;
    --sky:#9cc9ea;
    --hill:#8e9a6a;
    --sea:#1f7fc0;
    --skin:#e9c7b0;
    --shirt:#1d2a4a;
  }
  *{box-sizing:border-box;margin:0;padding:0}
  html,body{width:720px;height:1200px;overflow:hidden;background:var(--sheet);font-family:"Poppins",sans-serif}
  .banner{position:absolute;left:72px;width:576px;background:var(--white);overflow:hidden;box-shadow:0 10px 24px rgba(0,0,0,.22)}
  .banner--square{top:92px;height:576px}
  .banner--wide{top:800px;height:288px}
  .abs{position:absolute}
  .scene{position:absolute;left:0;top:0}
  .brand{position:absolute;text-align:center;font-weight:800;color:var(--orange);white-space:nowrap;transform:translateX(-50%)}
  .brand-mark{display:inline-block;background:var(--navy);vertical-align:middle}
  .tagline{position:absolute;transform:translateX(-50%);white-space:nowrap;font-weight:600;color:var(--navy);letter-spacing:1.6px;display:flex;align-items:center;gap:5px}
  .tagline::before,.tagline::after{content:"";display:block;width:18px;height:1px;background:var(--navy)}
  .headline{position:absolute;font-weight:800;line-height:1;white-space:nowrap;color:var(--navy);letter-spacing:-.2px}
  .headline .accent{color:var(--orange)}
  .rule{position:absolute;height:1.5px;background:var(--navy)}
  .pitch{position:absolute;color:var(--ink);white-space:nowrap;line-height:1.25}
  .pitch .accent{color:var(--orange)}
  .name-bar{position:absolute;background:var(--navy);color:var(--white);font-weight:600;white-space:nowrap;display:flex;align-items:center}
  .name-bar .accent,.footer-name .accent{color:var(--orange)}
  .phone{position:absolute;font-weight:700;color:var(--ink);white-space:nowrap}
  .cta{position:absolute;background:var(--orange);color:var(--white);font-weight:700;border-radius:9px;display:flex;align-items:center;justify-content:center;gap:5px;white-space:nowrap;box-shadow:0 4px 8px rgba(242,70,15,.35)}
  .cta-arrow{display:inline-block;background:var(--navy);border-radius:50%}
  .footer{position:absolute;left:0;width:576px;background:var(--navy)}
  .contact{position:absolute;color:var(--white);font-weight:600;white-space:nowrap;display:flex;align-items:center}
  .icon-dot{display:inline-flex;align-items:center;justify-content:center;border-radius:50%;background:var(--orange);border:1.5px solid var(--white)}
  .footer-name{position:absolute;color:var(--white);font-weight:700;white-space:nowrap}
  .portrait{position:absolute;background:linear-gradient(180deg,rgba(0,0,0,0) 0%,var(--skin) 10%,#dcae8f 45%,var(--shirt) 62%,var(--shirt) 100%);border-radius:48% 48% 0 0 / 28% 28% 0 0}
</style>
</head>
<body>

<!-- Square post -->
<section class="banner banner--square">
  <svg class="scene" width="576" height="576" viewBox="0 0 576 576" role="img" aria-label="Harbour photo: colourful houses on a rocky green hillside above blue water">
    <defs>
      <linearGradient id="harbourSq" x1="0" y1="0" x2="0" y2="1">
        <stop offset="0" stop-color="#a9d2ef"/>
        <stop offset=".22" stop-color="#9a9c86"/>
        <stop offset=".5" stop-color="#8a9a5e"/>
        <stop offset=".68" stop-color="#9b8e80"/>
        <stop offset=".75" stop-color="#2b8ccc"/>
        <stop offset="1" stop-color="#1d6ea8"/>
      </linearGradient>
    </defs>
    <circle cx="479" cy="102" r="196" fill="none" stroke="var(--orange)" stroke-width="3"/>
    <circle cx="479" cy="102" r="189" fill="none" stroke="var(--navy)" stroke-width="3"/>
    <circle cx="479" cy="102" r="185" fill="url(#harbourSq)"/>
  </svg>

  <div class="brand" style="left:127px;top:85px;font-size:16px">
    <span class="brand-mark" style="width:10px;height:10px;margin-right:6px"></span>BRIGHT HARBOUR MORTGAGES
  </div>
  <div class="tagline" style="left:127px;top:104px;font-size:6.5px">WE THINK OUTSIDE THE BOX</div>

  <div class="headline" style="left:31px;top:127px;font-size:31px">BUILDING YOUR</div>
  <div class="headline" style="left:30px;top:158px;font-size:36px"><span class="accent">DREAM HOME</span></div>
  <div class="headline" style="left:31px;top:194px;font-size:30.5px">ONE MORTGAGE</div>
  <div class="headline" style="left:31px;top:225px;font-size:30.5px"><span class="accent">AT A TIME</span></div>

  <div class="rule" style="left:31px;top:264px;width:332px"></div>
  <p class="pitch" style="left:31px;top:275px;font-size:13.2px">Let Us Help You Unlock Your <span class="accent">DREAM HOME TODAY</span><br>With Low Rates &amp; Great Deals!</p>

  <div class="name-bar" style="left:31px;top:326px;width:410px;height:49px;padding-left:13px;font-size:35px">MAREN&nbsp;<span class="accent">DOYLE</span></div>

  <svg class="abs" style="left:31px;top:389px" width="44" height="44" viewBox="0 0 44 44" aria-hidden="true">
    <circle cx="22" cy="22" r="21" fill="var(--orange)" stroke="var(--navy)" stroke-width="2"/>
    <path d="M15 12c1-1 2.5-1 3.2.2l2 3.4c.5.9.2 1.9-.6 2.5l-1.3 1c.9 2 2.6 3.8 4.6 4.7l1-1.3c.6-.8 1.7-1 2.5-.5l3.4 2c1.2.7 1.2 2.2.2 3.2l-1.6 1.6c-1.6 1.6-4.5 1.2-7.8-1.4-2.5-2-4.7-4.6-6-7.3-1.3-2.8-1.3-5.1.1-6.5z" fill="var(--white)"/>
  </svg>
  <div class="phone" style="left:89px;top:391px;font-size:29px">709-555-0142</div>

  <div class="cta" style="left:112px;top:439px;width:126px;height:24px;font-size:13px">GET STARTED
    <svg class="cta-arrow" width="16" height="16" viewBox="0 0 16 16" aria-hidden="true"><path d="M5 4l3 4-3 4M8.5 4l3 4-3 4" fill="none" stroke="var(--white)" stroke-width="1.8"/></svg>
  </div>

  <div class="footer" style="top:480px;height:96px"></div>
  <div class="contact" style="left:36px;top:499px;font-size:16.5px;gap:14px">
    <span class="icon-dot" style="width:27px;height:27px">
      <svg width="13" height="10" viewBox="0 0 13 10" aria-hidden="true"><rect x=".5" y=".5" width="12" height="9" rx="1.5" fill="var(--white)"/><path d="M1 1.5l5.5 4 5.5-4" fill="none" stroke="var(--orange)" stroke-width="1.2"/></svg>
    </span>info@brightharbourmtg.com
  </div>
  <div class="contact" style="left:36px;top:530px;font-size:16.5px;gap:14px">
    <span class="icon-dot" style="width:27px;height:27px">
      <svg width="14" height="14" viewBox="0 0 14 14" aria-hidden="true"><g fill="none" stroke="var(--white)" stroke-width="1.1"><circle cx="7" cy="7" r="6"/><ellipse cx="7" cy="7" rx="2.6" ry="6"/><path d="M1 7h12M2 4h10M2 10h10"/></g></svg>
    </span>www.brightharbourmtg.com
  </div>

  <div class="portrait" role="img" aria-label="Portrait photo of the broker" style="left:370px;top:296px;width:206px;height:280px"></div>
</section>

<!-- Wide post -->
<section class="banner banner--wide">
  <svg class="scene" width="576" height="288" viewBox="0 0 576 288" role="img" aria-label="Harbour photo: colourful houses on a rocky hillside above blue water">
    <defs>
      <linearGradient id="harbourWide" x1="0" y1="0" x2="0" y2="1">
        <stop offset="0" stop-color="#a9d2ef"/>
        <stop offset=".25" stop-color="#a3a590"/>
        <stop offset=".55" stop-color="#8b9960"/>
        <stop offset=".72" stop-color="#968a7c"/>
        <stop offset=".78" stop-color="#2b8ccc"/>
        <stop offset="1" stop-color="#1d6ea8"/>
      </linearGradient>
    </defs>
    <circle cx="440" cy="10" r="178" fill="none" stroke="var(--orange)" stroke-width="2.5"/>
    <circle cx="440" cy="10" r="172" fill="none" stroke="var(--navy)" stroke-width="2.5"/>
    <circle cx="440" cy="10" r="169" fill="url(#harbourWide)"/>
  </svg>

  <div class="brand" style="left:138px;top:72px;font-size:14px">
    <span class="brand-mark" style="width:9px;height:9px;margin-right:5px"></span>BRIGHT HARBOUR MORTGAGES
  </div>
  <div class="tagline" style="left:138px;top:89px;font-size:6px">WE THINK OUTSIDE THE BOX</div>

  <div class="headline" style="left:16px;top:106px;font-size:22.5px">BUILDING YOUR DREAM</div>
  <div class="headline" style="left:16px;top:129px;font-size:22.5px"><span class="accent">HOME ONE MORTGAGE</span></div>
  <div class="headline" style="left:17px;top:152px;font-size:22.5px">AT A TIME</div>

  <div class="rule" style="left:17px;top:184px;width:308px"></div>
  <p class="pitch" style="left:16px;top:194px;font-size:13px">Let Us Help You Unlock Your <span class="accent">DREAM HOME TODAY</span><br>With Low Rates &amp; Great Deals!</p>

  <div class="cta" style="left:354px;top:201px;width:126px;height:24px;font-size:13px">GET STARTED
    <svg class="cta-arrow" width="16" height="16" viewBox="0 0 16 16" aria-hidden="true"><path d="M5 4l3 4-3 4M8.5 4l3 4-3 4" fill="none" stroke="var(--white)" stroke-width="1.8"/></svg>
  </div>

  <div class="footer" style="top:239px;height:49px"></div>
  <div class="footer-name" style="left:16px;top:253px;font-size:13.5px">MAREN <span class="accent">DOYLE</span></div>
  <div class="contact" style="left:150px;top:256px;font-size:7.3px;gap:5px">
    <span class="icon-dot" style="width:13px;height:13px">
      <svg width="7" height="7" viewBox="0 0 44 44" aria-hidden="true"><path d="M10 5c2-2 5-2 6.4.4l4 6.8c1 1.8.4 3.8-1.2 5l-2.6 2c1.8 4 5.2 7.6 9.2 9.4l2-2.6c1.2-1.6 3.4-2 5-1l6.8 4c2.4 1.4 2.4 4.4.4 6.4l-3.2 3.2c-3.2 3.2-9 2.4-15.6-2.8-5-4-9.4-9.2-12-14.6C6.4 16 6.4 11.4 10 5z" fill="var(--white)"/></svg>
    </span>709-555-0142
  </div>
  <div class="contact" style="left:230px;top:256px;font-size:7.3px;gap:5px">
    <span class="icon-dot" style="width:13px;height:13px">
      <svg width="7" height="6" viewBox="0 0 13 10" aria-hidden="true"><rect x=".5" y=".5" width="12" height="9" rx="1.5" fill="var(--white)"/><path d="M1 1.5l5.5 4 5.5-4" fill="none" stroke="var(--orange)" stroke-width="1.4"/></svg>
    </span>info@brightharbourmtg.com
  </div>
  <div class="contact" style="left:363px;top:256px;font-size:7.3px;gap:5px">
    <span class="icon-dot" style="width:13px;height:13px">
      <svg width="8" height="8" viewBox="0 0 14 14" aria-hidden="true"><g fill="none" stroke="var(--white)" stroke-width="1.3"><circle cx="7" cy="7" r="6"/><ellipse cx="7" cy="7" rx="2.6" ry="6"/><path d="M1 7h12"/></g></svg>
    </span>www.brightharbourmtg.com
  </div>

  <div class="portrait" role="img" aria-label="Portrait photo of the broker" style="left:495px;top:177px;width:81px;height:111px"></div>
</section>

</body>
</html>
```